Embroidery Teacher

I design and teach small embroidery classes, I am based in South Australia
The majority of my embroidery is done on bright wool fabrics and the designs are naive / folk art type birds, flowers and houses. The finished products stitched by the ladies in my classes are usually made into book covers, needle keepers or small quilts.

Industry/Entity Type

Embroidery

Contact Information for Business Card

Rosalind Hatchett
PO Box 3817
Fernvale SA 5092
M. 0427183592
E. ros@merrythreadwork.com.au

```html
<!DOCTYPE html>
<html lang="en">
<head>
<meta charset="utf-8">
<title>Rosalind Hatchett – Business Card</title>
<link rel="stylesheet" href="https://fonts.googleapis.com/css2?family=Questrial&display=swap">
<style>
  :root {
    --backdrop: #ece6dc;
    --card-white: #ffffff;
    --orange: #ea7a1c;
    --orange-light: #f28a25;
    --orange-deep: #e06f17;
    --plum: #2a0f1c;
    --ink: #2a1a22;
    --text: #3a2f33;
    --berry: #d9356a;
  }
  html, body {
    margin: 0;
    width: 1200px;
    height: 1023px;
    overflow: hidden;
    background: var(--backdrop);
    font-family: "Questrial", "Century Gothic", sans-serif;
  }
  .sheet {
    width: 1200px;
    height: 1023px;
    display: flex;
    flex-direction: column;
    align-items: center;
    justify-content: center;
    gap: 60px;
  }
  .card {
    position: relative;
    width: 540px;
    height: 330px;
    box-shadow: 0 10px 28px rgba(60, 40, 20, 0.22);
    overflow: hidden;
  }
  /* Front */
  .card-front { background: var(--card-white); }
  .card-front .side-band {
    position: absolute;
    top: 0; right: 0;
    width: 72px;
    height: 100%;
    background: var(--orange-deep);
  }
  .card-front .side-band::after {
    content: "";
    position: absolute;
    left: 0; right: 0; bottom: 0;
    height: 38%;
    background: var(--orange-light);
  }
  .card-front .content {
    position: absolute;
    left: 0; top: 0;
    width: 468px;
    height: 100%;
  }
  .name-row {
    position: absolute;
    top: 128px;
    left: 0;
    width: 100%;
    display: flex;
    align-items: center;
  }
  .rule {
    flex: 1;
    height: 3px;
    background: var(--orange);
  }
  .name {
    margin: 0 12px;
    font-size: 30px;
    font-weight: 400;
    color: var(--ink);
    letter-spacing: 0.5px;
    white-space: nowrap;
  }
  .details {
    position: absolute;
    top: 182px;
    left: 0;
    width: 100%;
    text-align: center;
    font-size: 14.5px;
    line-height: 26px;
    color: var(--text);
  }
  .details p { margin: 0; }
  /* Back */
  .card-back { background: var(--orange); }
  .card-back .plum-strip {
    position: absolute;
    top: 0; left: 0;
    width: 92px;
    height: 100%;
    background: var(--plum);
  }
  .card-back .stitched-art {
    position: absolute;
    left: 170px;
    top: 60px;
    width: 300px;
    height: 210px;
    border-radius: 8px;
    background: radial-gradient(ellipse at 45% 55%, #3a1428 0%, #5a1f3a 45%, rgba(217, 53, 106, 0.55) 75%, rgba(234, 122, 28, 0) 100%);
  }
</style>
</head>
<body>
  <main class="sheet">
    <section class="card card-front" aria-label="Business card front">
      <div class="content">
        <div class="name-row">
          <span class="rule"></span>
          <h1 class="name">Rosalind Hatchett</h1>
          <span class="rule"></span>
        </div>
        <div class="details">
          <p>M: 0427183592 / E: ros@merrythreadwork.com.au</p>
          <p>PO Box 3817, Fernvale SA 5092</p>
        </div>
      </div>
      <div class="side-band"></div>
    </section>

    <section class="card card-back" aria-label="Business card back">
      <div class="plum-strip"></div>
      <div class="stitched-art" role="img" aria-label="Embroidered folk-art bird in plum wool with pink and green stitching on orange fabric"></div>
    </section>
  </main>
</body>
</html>
```